A website serving business owners or those wishing to become business owners.

A website serving those in the service industry or would like to get started with their own business. From business licensing , marketing, business loans, and much more.

We offer business incubation services as well as further growth assistance.

Including, but not limited to...

marketing
websites
seo
brindle ads
social media ads
logos
business licensing assistance
customer acquisition and ongoing coordination
1. scheduling
2 customer support
3.coordination between business owners and clients

Cleaning training program/courses.

Target Market(s)

Hispanic folks looking to start or grow their cleaning company.

Industry/Entity Type

business incubation and growth support.

Coding

Coded - Design and coding required

Font styles to use
Sans Serif

Requirements
Must have
• wordpress, custom design
Nice to have
• something similar to this .... https://www.tallvesper.com/
Should not have
• no predesigned themes, no third party templates

```html
<!DOCTYPE html>
<html lang="en">
<head>
<meta charset="utf-8">
<title>Firm Nova — Business Incubation &amp; Growth</title>
<link href="https://fonts.googleapis.com/css2?family=Poppins:wght@400;500;600;700;800&display=swap" rel="stylesheet">
<style>
:root{
  --accent:#3cb6e3;
  --title-blue:#1b5aa6;
  --ink:#111418;
  --body:#4a4f55;
  --soft-bg:#e6eff7;
  --footer:#2f3033;
  --footer-bar:#28292b;
  --white:#ffffff;
}
*{margin:0;padding:0;box-sizing:border-box}
html,body{width:1200px;height:4847px;overflow:hidden;background:var(--white)}
body{font-family:'Poppins',sans-serif;color:var(--ink);position:relative}
.abs{position:absolute}
.btn{position:absolute;display:flex;align-items:center;justify-content:center;background:var(--accent);color:#fff;font-size:13px;font-weight:600;letter-spacing:.5px;text-transform:uppercase}
.photo{position:absolute}

/* header */
.site-header{position:absolute;top:0;left:0;width:1200px;height:96px;background:#fff}
.brand{position:absolute;left:71px;top:22px;display:flex;align-items:center;gap:14px}
.brand-mark{width:44px;height:44px;border-radius:50%;background:var(--accent)}
.brand-name{font-size:28px;font-weight:600;color:#2a2f36;line-height:1}
.brand-tag{font-size:12px;color:#8a8f96;margin-top:4px}
.main-nav{position:absolute;right:50px;top:40px;display:flex;gap:38px;font-size:14px;font-weight:600}
.main-nav a{color:#222;text-decoration:none}
.main-nav a.active{color:var(--accent)}

/* hero */
.hero{position:absolute;top:96px;left:0;width:1200px;height:690px;background:linear-gradient(90deg,#000 0%,#0b0b0c 30%,#5d636b 60%,#8c8f92 100%)}
.hero-title{position:absolute;left:77px;top:178px;color:#fff;font-weight:800;line-height:1}
.hero-title .small{display:block;font-size:44px;letter-spacing:.5px}
.hero-title .big{display:block;font-size:66px;margin-top:6px}
.hero-sub{position:absolute;left:77px;top:298px;color:#fff;font-size:24px;line-height:36px;width:520px}
.dots{position:absolute;left:75px;top:538px;display:flex;gap:12px}
.dots span{width:12px;height:12px;border-radius:50%;border:2px solid var(--accent)}
.dots span.on{background:#fff;border-color:#fff}
.hero-wave{position:absolute;left:0;top:680px}

/* about */
.who-card{position:absolute;left:587px;top:909px;width:538px;height:413px;background:#fff;box-shadow:0 4px 24px rgba(0,0,0,.12);padding:32px 28px}
.who-card h2{font-size:34px;font-weight:700;margin-bottom:12px}
.who-card p{font-size:14px;line-height:28.6px;color:#333}

/* sections */
.section-title{position:absolute;left:0;width:1200px;text-align:center;font-size:35px;font-weight:700;color:var(--ink)}
.services{position:absolute;top:1452px;left:0;width:1200px;height:912px;background:var(--soft-bg)}
.svc{position:absolute;width:241px;text-align:center}
.svc .pic{height:174px;width:241px}
.svc h3{color:var(--title-blue);font-size:22px;font-weight:600;line-height:28px;margin-top:14px}
.svc p{font-size:14px;line-height:24px;color:#444;margin-top:6px}

.why{position:absolute;width:329px;text-align:center}
.why .pic{height:256px}
.why h3{background:#fff;margin:-20px auto 0;width:290px;position:relative;color:var(--title-blue);font-size:22px;font-weight:600;padding-top:8px;height:40px}
.why p{font-size:14px;line-height:26px;color:#444;margin-top:6px;padding:0 20px}

.facts{position:absolute;top:2953px;left:0;width:1200px;height:412px;background:radial-gradient(ellipse at 55% 30%,#2a7fd0 0%,#1360b3 45%,#0a3f85 100%)}
.fact{position:absolute;width:260px;text-align:center;color:#fff}
.fact svg{display:block;margin:0 auto}
.fact .num{font-size:62px;font-weight:700;line-height:1;margin-top:18px}
.fact .lbl{font-size:16px;margin-top:4px}

.post{position:absolute;width:329px}
.post .pic{height:202px}
.post h3{font-size:22px;font-weight:600;line-height:34px;margin-top:34px;color:#222}
.post .date{font-size:14px;color:var(--accent);font-weight:500;margin-top:6px}
.post p{font-size:15px;line-height:27px;color:#444;margin-top:12px}
.arrow{position:absolute;top:3690px}

.trusted{position:absolute;top:4006px;left:0;width:1200px;height:345px;background:var(--soft-bg);text-align:center}
.trusted h2{position:absolute;top:70px;width:1200px;font-size:35px;font-weight:700;color:var(--title-blue)}
.trusted p{position:absolute;top:124px;left:150px;width:900px;font-size:19px;line-height:36px;color:#444}

.site-footer{position:absolute;top:4351px;left:0;width:1200px;height:370px;background:var(--footer);color:#fff}
.site-footer h4{font-size:24px;font-weight:700;margin-bottom:16px}
.fcol{position:absolute;top:52px}
.fcol p{font-size:14px;line-height:27px;color:#e4e4e4}
.addr li{list-style:none;display:flex;gap:14px;font-size:17px;line-height:32px;margin-bottom:8px}
.addr svg{flex:none;margin-top:8px}
.socials{display:flex;gap:22px;margin:18px 0 0 0}
.socials span{width:20px;height:20px;border-radius:50%;background:#fff}
.field{width:331px;height:49px;background:#fff;color:#555;font-size:14px;padding:0 16px;display:flex;align-items:center;margin-bottom:9px}
.submit{width:331px;height:47px;background:var(--accent);color:#fff;font-size:14px;font-weight:600;display:flex;align-items:center;justify-content:center}
.footer-bar{position:absolute;top:4721px;left:0;width:1200px;height:126px;background:var(--footer-bar);color:#ddd;text-align:center}
.footer-bar nav{display:flex;justify-content:center;gap:42px;font-size:13px;margin-top:38px}
.footer-bar small{display:block;font-size:13px;margin-top:12px}
</style>
</head>
<body>

<header class="site-header">
  <div class="brand">
    <span class="brand-mark"></span>
    <div><div class="brand-name">BrightPath</div><div class="brand-tag">Makes Successful Business</div></div>
  </div>
  <nav class="main-nav">
    <a class="active">HOME</a><a>ABOUT US</a><a>SERVICES</a><a>PROJECTS</a><a>BLOG</a><a>CONTACT</a><a>SHOP</a>
  </nav>
</header>

<section class="hero">
  <div class="photo" role="img" aria-label="Team of colleagues planning on a glass board" style="left:600px;top:0;width:600px;height:690px;background:linear-gradient(120deg,rgba(40,40,40,0) 0%,rgba(150,140,130,.35) 50%,rgba(90,100,110,.3) 100%)"></div>
  <h1 class="hero-title"><span class="small">WELCOME TO</span><span class="big">FIRM NOVA</span></h1>
  <p class="hero-sub">We offer business incubation services as well as further growth assistance.</p>
  <a class="btn" style="left:75px;top:397px;width:179px;height:47px">Read More</a>
  <div class="dots"><span class="on"></span><span></span><span></span><span></span></div>
</section>
<svg class="hero-wave" width="1200" height="110" viewBox="0 0 1200 110">
  <path d="M0 12 Q600 90 1200 0 L1200 110 L0 110 Z" fill="#fff"/>
  <path d="M0 12 Q600 90 1200 0 L1200 4 Q600 120 0 18 Z" fill="var(--accent)"/>
</svg>

<section>
  <div class="photo" role="img" aria-label="Business meeting around a table with a tablet" style="left:75px;top:861px;width:598px;height:508px;background:linear-gradient(135deg,#4c4a42,#8a8170 55%,#c9c2b4)"></div>
  <div class="who-card">
    <h2>WHO WE ARE</h2>
    <p>We are Lumora located in newyork city,USA. It is a long established fact that a reader will be distracted by the readable content pleasure and praising pain was born and I will give you a complete account of the system, and expound the actual teachings of the great explorer of the master-builder of human happiness. We have built an enviable reputation in the consumer goods, heavy industry, high-tech.</p>
    <a class="btn" style="left:28px;top:329px;width:179px;height:49px">Read More</a>
  </div>
</section>

<section class="services">
  <h2 class="section-title" style="top:56px">OUR SERVICES</h2>
  <div class="svc" style="left:75px;top:137px"><div class="pic" role="img" aria-label="Marketing desk with laptop" style="background:linear-gradient(135deg,#6b5a48,#b9a58c)"></div><h3>Marketing</h3><p>Sed ut perspiciatis unde omnis iste natus error sit vol.</p></div>
  <div class="svc" style="left:344px;top:137px"><div class="pic" role="img" aria-label="Person building a website" style="background:linear-gradient(135deg,#9aa4ab,#e3e6e8)"></div><h3>Websites</h3><p>Sed ut perspiciatis unde omnis iste natus error sit vol.</p></div>
  <div class="svc" style="left:615px;top:137px"><div class="pic" role="img" aria-label="Digital SEO concept" style="background:linear-gradient(135deg,#06243a,#0f6e8e)"></div><h3>SEO</h3><p>Sed ut perspiciatis unde omnis iste natus error sit vol.</p></div>
  <div class="svc" style="left:886px;top:137px"><div class="pic" role="img" aria-label="Ad dashboard on laptop" style="background:linear-gradient(135deg,#3a3d44,#dfe6f0)"></div><h3>Brindle Ads</h3><p>Sed ut perspiciatis unde omnis iste natus error sit vol.</p></div>
  <div class="svc" style="left:75px;top:453px"><div class="pic" role="img" aria-label="Social media sketches on desk" style="background:linear-gradient(135deg,#c7553f,#7fb6b2)"></div><h3>Social Media Ads</h3><p>Sed ut perspiciatis unde omnis iste natus error sit vol.</p></div>
  <div class="svc" style="left:344px;top:453px"><div class="pic" role="img" aria-label="Logo design sketches" style="background:linear-gradient(135deg,#8f8c88,#d9d6d1)"></div><h3>Logos</h3><p>Sed ut perspiciatis unde omnis iste natus error sit vol.</p></div>
  <div class="svc" style="left:615px;top:453px"><div class="pic" role="img" aria-label="Businessman reviewing documents" style="background:linear-gradient(135deg,#dfe3e8,#2f4a6e)"></div><h3>Business Licensing Assistance</h3><p>Sed ut perspiciatis unde omnis iste natus error sit vol.</p></div>
  <div class="svc" style="left:886px;top:453px"><div class="pic" role="img" aria-label="Trainer presenting to a class" style="background:linear-gradient(135deg,#2a2d30,#e2e5e4)"></div><h3>Cleaning Training</h3><p>Sed ut perspiciatis unde omnis iste natus error sit vol.</p></div>
  <a class="btn" style="left:512px;top:796px;width:176px;height:49px">View All</a>
</section>

<section>
  <h2 class="section-title" style="top:2416px">WHY CHOOSE US</h2>
  <div class="why" style="left:75px;top:2497px"><div class="pic" role="img" aria-label="Team working at a shared table from above" style="background:linear-gradient(135deg,#4a3526,#a77a55)"></div><h3>About Our Business</h3><p>How all this mistaken idea denouncing pleasure and praising pain was born system.</p></div>
  <div class="why" style="left:436px;top:2497px"><div class="pic" role="img" aria-label="Analytics charts on a laptop" style="background:linear-gradient(135deg,#e9e9e9,#9a8c7c)"></div><h3>Advanced Analytics</h3><p>The great explorer of the truth master builder of human happiness avoids pleasure.</p></div>
  <div class="why" style="left:798px;top:2497px"><div class="pic" role="img" aria-label="Presenter in a bright meeting room" style="background:linear-gradient(135deg,#2c3138,#c9d3dc)"></div><h3>Customer Insights</h3><p>There anyone who loves or pursues or desires to pain itself occasionally circumstances.</p></div>
</section>

<section class="facts">
  <h2 class="section-title" style="top:52px;color:#fff">INTERESTING FACTS</h2>
  <div class="fact" style="left:66px;top:152px">
    <svg width="100" height="80" viewBox="0 0 100 80" fill="none" stroke="#fff" stroke-width="3"><ellipse cx="40" cy="30" rx="30" ry="20"/><path d="M24 46 L18 60 L34 49"/><ellipse cx="66" cy="46" rx="24" ry="16"/></svg>
    <div class="num">107</div><div class="lbl">Experienced Consultants</div></div>
  <div class="fact" style="left:335px;top:152px">
    <svg width="100" height="80" viewBox="0 0 100 80" fill="none" stroke="#fff" stroke-width="3"><rect x="20" y="40" width="14" height="36" rx="3"/><path d="M34 44 L48 24 L52 6 Q62 6 60 24 L80 26 Q86 28 84 36 L78 70 Q76 76 68 76 L34 74"/></svg>
    <div class="num">2000</div><div class="lbl">Sucessfull Projects</div></div>
  <div class="fact" style="left:605px;top:152px">
    <svg width="100" height="80" viewBox="0 0 100 80" fill="none" stroke="#fff" stroke-width="3"><path d="M30 6 H70 V30 Q70 50 50 52 Q30 50 30 30 Z"/><path d="M30 12 H18 Q18 32 32 34 M70 12 H82 Q82 32 68 34"/><path d="M50 52 V64 M36 74 H64 V66 H36 Z"/></svg>
    <div class="num">47</div><div class="lbl">Winning Awards</div></div>
  <div class="fact" style="left:876px;top:152px">
    <svg width="110" height="80" viewBox="0 0 110 80" fill="none" stroke="#fff" stroke-width="3"><circle cx="55" cy="22" r="13"/><path d="M32 70 Q34 42 55 42 Q76 42 78 70 Z"/><circle cx="22" cy="34" r="9"/><path d="M6 70 Q8 50 24 50"/><circle cx="88" cy="34" r="9"/><path d="M104 70 Q102 50 86 50"/></svg>
    <div class="num">100%</div><div class="lbl">Satisfied Customers</div></div>
</section>

<section>
  <h2 class="section-title" style="top:3409px">LATEST FROM BLOG</h2>
  <svg class="arrow" style="left:36px" width="20" height="36" viewBox="0 0 20 36"><path d="M18 2 L2 18 L18 34" fill="none" stroke="#999" stroke-width="2"/></svg>
  <svg class="arrow" style="left:1142px" width="20" height="36" viewBox="0 0 20 36"><path d="M2 2 L18 18 L2 34" fill="none" stroke="#999" stroke-width="2"/></svg>
  <article class="post" style="left:75px;top:3489px"><div class="pic" role="img" aria-label="Rising growth arrow over charts" style="background:linear-gradient(135deg,#dbe8f5,#8db3d8)"></div><h3>Successfull business tips in 2017: way to grow</h3><div class="date">FEB 17, 2024</div><p>Pursues or desires to obtain pain of itself our because it is pain, but because occasionally can procure great pleasure.</p></article>
  <article class="post" style="left:436px;top:3489px"><div class="pic" role="img" aria-label="Support agents with headsets" style="background:linear-gradient(135deg,#e6e8ea,#1f4f9a)"></div><h3>Successfull business tips in 2017: way to grow</h3><div class="date">FEB 17, 2024</div><p>Pursues or desires to obtain pain of itself our because it is pain, but because occasionally can procure great pleasure.</p></article>
  <article class="post" style="left:798px;top:3489px"><div class="pic" role="img" aria-label="Colleagues reviewing data on screens" style="background:linear-gradient(135deg,#17324f,#8a7a6a)"></div><h3>Successfull business tips in 2017: way to grow</h3><div class="date">FEB 17, 2024</div><p>Pursues or desires to obtain pain of itself our because it is pain, but because occasionally can procure great pleasure.</p></article>
</section>

<section class="trusted">
  <h2>TRUSTED BY OVER 10,000 LOCAL BUSINESSES</h2>
  <p>How all this mistaken idea of denouncing pleasure and praising pain was born and I will give you a complete account of the system expound.</p>
  <a class="btn" style="left:512px;top:222px;width:176px;height:48px">Join With Us</a>
</section>

<footer class="site-footer">
  <div class="fcol" style="left:75px;width:320px">
    <h4>ABOUT US</h4>
    <p>Our consulting 20 years of experience we'll ensure you always get the best guidance for our customers,<br>We have built an enviable reputation in the consumer goods,</p>
  </div>
  <div class="fcol" style="left:442px;width:320px">
    <h4>ADDRESS</h4>
    <ul class="addr">
      <li><svg width="18" height="16" viewBox="0 0 18 16"><path d="M1 3 L6 1 L12 3 L17 1 V13 L12 15 L6 13 L1 15 Z" fill="var(--accent)"/></svg><span>Maple Row, Springfield,<br>SP 40218</span></li>
      <li><svg width="18" height="18" viewBox="0 0 18 18"><path d="M4 1 L7 5 L5 7 Q7 11 11 13 L13 11 L17 14 L15 17 Q6 16 1 3 Z" fill="var(--accent)"/></svg><span>+1 555-010-4477</span></li>
      <li><svg width="18" height="14" viewBox="0 0 18 14"><rect width="18" height="14" rx="2" fill="var(--accent)"/><path d="M1 2 L9 8 L17 2" stroke="#2f3033" stroke-width="1.6" fill="none"/></svg><span>admin@firmnova.com</span></li>
    </ul>
    <div class="socials"><span></span><span></span><span></span><span></span><span></span></div>
  </div>
  <div class="fcol" style="left:794px;width:331px">
    <h4>SUBSCRIBE US</h4>
    <div class="field">Name</div>
    <div class="field">Email Address</div>
    <div class="submit">SUBMIT NOW</div>
  </div>
</footer>
<div class="footer-bar">
  <nav><span>HOME</span><span>ABOUT US</span><span>SERVICES</span><span>PROJECTS</span><span>BLOG</span><span>CONTACT</span><span>SHOP</span></nav>
  <small>Copyright © 2024 CompanyName All rights reserved</small>
</div>

</body>
</html>
```